50th Anniversary Gala Save the date Postcard 8.5x5.5 inches

Looking for a 5.5x8.5 in one-sided postcard design for our annual gala. Design needs to include "Save the date" prominently with all the event information included below. Design should be light, include the colors of our logo and elegant. (almost like a wedding save the date). "Bridges of Grace" should look like its own logo.

50th Anniversary Gala at The Lodge at Birchmere Glen – “Bridges of Grace – Celebrating 50 Years of Building Community”
Thursday, October 24
6-11p
The Lodge at Birchmere Glen
Calloway Parkway, Ashford Vale, NJ
Honoring – TRB Previous Presidents

Target Market(s)

Exisiting donors

Industry/Entity Type

nonprofit

Font styles to use
Serif
Script

Requirements
Must have
• Save the date prominent
Should not have
• should not have a dark background

```html
<!DOCTYPE html>
<html lang="en">
<head>
<meta charset="utf-8">
<title>Save the Date – 50th Anniversary Gala</title>
<link rel="stylesheet" href="https://fonts.googleapis.com/css2?family=EB+Garamond:wght@500&family=Montserrat:wght@600&family=Parisienne&display=swap">
<style>
  :root {
    --backdrop: #1b2d44;
    --navy: #1b4a8a;
    --gold: #d9a93c;
    --green: #6aa83a;
    --sky: #1d8fd4;
    --white: #ffffff;
    --pale: #eef6dc;
    --leaf: #8cc63f;
  }
  html, body {
    margin: 0;
    padding: 0;
    width: 1200px;
    height: 1200px;
    overflow: hidden;
    background: var(--backdrop);
  }
  .postcard {
    position: absolute;
    left: 50px;
    top: 232px;
    width: 1097px;
    height: 720px;
    overflow: hidden;
    background:
      radial-gradient(ellipse 60% 45% at 30% 15%, rgba(255,255,255,0.75), rgba(255,255,255,0) 70%),
      radial-gradient(ellipse 50% 40% at 78% 72%, rgba(235,240,225,0.7), rgba(235,240,225,0) 70%),
      radial-gradient(ellipse 55% 40% at 20% 85%, rgba(93,143,51,0.55), rgba(93,143,51,0) 75%),
      radial-gradient(ellipse 45% 35% at 95% 90%, rgba(80,125,45,0.6), rgba(80,125,45,0) 75%),
      linear-gradient(180deg, var(--pale) 0%, #d7e9b0 35%, #a9d160 70%, var(--leaf) 100%);
  }
  .org-name {
    position: absolute;
    left: 37px;
    top: 66px;
    width: 260px;
    display: flex;
    align-items: center;
    gap: 10px;
    font-family: "EB Garamond", serif;
    font-weight: 500;
    font-size: 27px;
    line-height: 1.1;
    color: var(--navy);
  }
  .org-name .dot {
    flex: none;
    width: 22px;
    height: 22px;
    border-radius: 50%;
    background: var(--gold);
  }
  .floral {
    position: absolute;
    right: 0;
    top: 0;
    width: 304px;
    height: 284px;
    border-bottom-left-radius: 70% 80%;
    background: radial-gradient(ellipse 75% 75% at 75% 30%, #cfe4f5 0%, #7dbbe8 35%, #4ea6de 55%, rgba(110,170,80,0.6) 80%, rgba(110,170,80,0) 100%);
  }
  .centered {
    position: absolute;
    left: 0;
    width: 100%;
    text-align: center;
    margin: 0;
  }
  .headline {
    top: 204px;
    font-family: "Parisienne", cursive;
    font-weight: 400;
    font-size: 138px;
    line-height: 1;
    color: var(--navy);
  }
  .event-line {
    top: 328px;
    font-family: "EB Garamond", serif;
    font-weight: 500;
    font-size: 26px;
    line-height: 1;
    font-variant-numeric: lining-nums;
    color: var(--navy);
  }
  .event-line .bullet {
    display: inline-block;
    width: 10px;
    height: 10px;
    border-radius: 50%;
    vertical-align: middle;
    margin: 0 28px;
  }
  .bullet.green { background: var(--green); }
  .bullet.sky { background: var(--sky); }
  .event-title {
    top: 371px;
    font-family: "Montserrat", sans-serif;
    font-weight: 600;
    font-size: 90px;
    line-height: 1;
    letter-spacing: 1px;
    -webkit-text-stroke: 1.5px var(--white);
    paint-order: stroke fill;
  }
  .event-title .w1 { color: var(--gold); }
  .event-title .w2 { color: var(--green); }
  .event-title .w3 { color: var(--sky); }
  .tagline {
    top: 476px;
    font-family: "Parisienne", cursive;
    font-size: 44px;
    line-height: 1;
    color: var(--navy);
  }
  .date-band {
    position: absolute;
    left: 395px;
    top: 552px;
    width: 296px;
    height: 32px;
    border-top: 1.5px solid var(--navy);
    border-bottom: 1.5px solid var(--navy);
    display: flex;
    align-items: center;
    justify-content: center;
    gap: 22px;
    font-family: "EB Garamond", serif;
    font-weight: 500;
    font-size: 21px;
    font-variant-numeric: lining-nums;
    color: var(--white);
  }
  .details {
    font-family: "EB Garamond", serif;
    font-weight: 500;
    font-size: 21px;
    line-height: 1;
    color: var(--white);
  }
  .details.venue { top: 598px; }
  .details.address { top: 632px; }
  .details.honoree { top: 666px; color: var(--navy); }
</style>
</head>
<body>
  <main class="postcard">
    <div class="org-name"><span class="dot"></span><span>Harborlight Neighbors</span></div>
    <div class="floral" role="img" aria-label="Watercolor illustration of blue roses with green leaves and buds"></div>

    <h1 class="centered headline">Save the Date</h1>
    <p class="centered event-line"><span class="bullet green"></span>50th Anniversary Gala at The Lodge at Birchmere Glen<span class="bullet sky"></span></p>
    <h2 class="centered event-title"><span class="w1">Bridges</span> <span class="w2">of</span> <span class="w3">Grace</span></h2>
    <p class="centered tagline">Celebrating 50 Years of Building Community</p>

    <div class="date-band"><span>Thursday, October 24</span><span>|</span><span>6-11p</span></div>
    <p class="centered details venue">The Lodge at Birchmere Glen</p>
    <p class="centered details address">Calloway Parkway, Ashford Vale, NJ</p>
    <p class="centered details honoree">Honoring – TRB Previous Presidents</p>
  </main>
</body>
</html>
```